Coffee Shop needs a fresh new menu

Hi,
I would like a new menu to be designed for our coffee shop.
We display our menu on a television screen, so would need it in a file that would allow us to continue to do so -- I have attached a photo so that you can see our current design, and how it is displayed.

I'd like something that is easy to read, if the design could have a "hipster" feel to it -- we are located at a hospital and University.

I have attached a Word file with what we would like on the menu.

Feel free to contact me if you have any questions.

Thanks,
Liv

Just A4 size will be fine, and no need to include menu 1 and menu 2 - I just put them in as an example of what we already have -- they are our printed menu's. Thanks

Hospital

```html
<!DOCTYPE html>
<html lang="en">
<head>
<meta charset="utf-8">
<title>Ward Café Menu</title>
<link rel="stylesheet" href="https://fonts.googleapis.com/css2?family=Bowlby+One&family=Quicksand:wght@500;600&display=swap">
<style>
  :root {
    --wood-dark: #141414;
    --wood-mid: #2b2b2b;
    --panel: #ebd3d3;
    --panel-edge: #c9a9a9;
    --band: #6a2c31;
    --band-text: #ffffff;
    --ink: #1d1416;
    --title-red: #d2262e;
    --title-shadow: #3a0d10;
    --coffee-tone: #8a5a3c;
    --muffin-tone: #c99a63;
    --plate-tone: #e6c7a0;
    --wrap-tone: #d7a86e;
  }
  * { margin: 0; padding: 0; box-sizing: border-box; }
  html, body { width: 1200px; height: 848px; overflow: hidden; }
  body {
    position: relative;
    background: linear-gradient(100deg, var(--wood-dark) 0%, var(--wood-mid) 35%, #1c1c1c 60%, var(--wood-mid) 85%, var(--wood-dark) 100%);
    font-family: "Quicksand", sans-serif;
    font-weight: 600;
    color: var(--ink);
  }
  .menu-title {
    position: absolute; top: 2px; left: 0; width: 1190px;
    text-align: center;
    font-family: "Bowlby One", sans-serif;
    font-size: 74px; letter-spacing: 4px; line-height: 90px;
    color: var(--title-red);
    text-shadow: 3px 3px 0 var(--title-shadow), -1px -1px 0 var(--title-shadow);
  }
  .panel {
    position: absolute;
    background: var(--panel);
    border: 1px solid var(--panel-edge);
    box-shadow: 0 0 8px rgba(0,0,0,.6);
    overflow: hidden;
  }
  .panel-band {
    position: absolute; left: 0; right: 0; height: 28px;
    background: var(--band); color: var(--band-text);
    font-size: 21px; font-weight: 500; line-height: 28px;
  }
  .food-image { position: absolute; opacity: .45; }
  .coffee-panel { left: 75px; top: 92px; width: 486px; height: 434px; }
  .light-panel { left: 75px; top: 560px; width: 486px; height: 272px; }
  .breakfast-panel { left: 646px; top: 92px; width: 488px; height: 289px; }
  .hot-panel { left: 646px; top: 446px; width: 488px; height: 386px; }
  .row { position: absolute; left: 0; right: 0; height: 22px; font-size: 16.5px; line-height: 22px; white-space: nowrap; }
  .row span { position: absolute; top: 0; }
  .extras-title { font-size: 19px; }
  .extras-line { font-size: 14px; }
  .extras-line .price { font-size: 17px; }
  .store-note { position: absolute; left: 26px; top: 328px; font-size: 13px; line-height: 20px; font-weight: 500; }
  .brand { position: absolute; left: 1058px; top: 700px; display: flex; align-items: center; gap: 6px; }
  .brand-dot { width: 26px; height: 26px; border-radius: 50%; background: #ffffff; }
  .brand-name { font-size: 18px; font-weight: 600; color: var(--title-red); }
</style>
</head>
<body>
  <h1 class="menu-title">MENU</h1>

  <section class="panel coffee-panel">
    <div class="food-image" role="img" aria-label="Cup of coffee on a saucer surrounded by coffee beans" style="left:100px;top:48px;width:386px;height:340px;background:radial-gradient(ellipse at 60% 40%, #f3e6da 0 22%, var(--coffee-tone) 40%, transparent 72%);"></div>
    <h2 class="panel-band" style="top:18px;padding-left:5px;">Coffee:</h2>
    <div class="row" style="top:63px"><span style="left:5px">Latte</span><span style="left:250px">small $4.0</span><span style="left:374px">Large $4.50</span></div>
    <div class="row" style="top:84px"><span style="left:5px">Cappuccino</span><span style="left:250px">small $4.0</span><span style="left:374px">Large $4.50</span></div>
    <div class="row" style="top:104px"><span style="left:5px">Flat White</span><span style="left:250px">small $4.0</span><span style="left:374px">Large $4.50</span></div>
    <div class="row" style="top:125px"><span style="left:5px">Long Black</span><span style="left:250px">small $4.0</span><span style="left:374px">Large $4.50</span></div>
    <div class="row" style="top:145px"><span style="left:5px">Hot Chocolate</span><span style="left:250px">small $4.0</span><span style="left:374px">Large $4.50</span></div>
    <div class="row" style="top:186px"><span style="left:5px">Chai Latte</span><span style="left:250px">small $4.50</span><span style="left:374px">Large $5.0</span></div>
    <div class="row" style="top:207px"><span style="left:5px">Mocha</span><span style="left:250px">small $4.50</span><span style="left:374px">Large $5.0</span></div>
    <div class="row" style="top:227px"><span style="left:5px">Dirty Chai</span><span style="left:250px">small $5</span><span style="left:374px">Large $5.50</span></div>
    <div class="row" style="top:269px"><span style="left:5px">Espresso</span><span style="left:293px">$3.50</span></div>
    <div class="row" style="top:289px"><span style="left:5px">Short Macchiato</span><span style="left:293px">$4.0</span></div>
    <div class="row" style="top:309px"><span style="left:5px">Piccolo</span><span style="left:293px">$4.0</span></div>
    <div class="row" style="top:330px"><span style="left:5px">Long Macchiato</span><span style="left:293px">$4.50</span></div>
    <div class="row extras-title" style="top:373px"><span style="left:5px">Extras</span></div>
    <div class="row extras-line" style="top:395px"><span style="left:5px">Soy Milk/Lactose Free Milk/Syrups/Extra Shot/Decaf</span><span class="price" style="left:370px">$0.50 extra</span></div>
  </section>

  <section class="panel light-panel">
    <div class="food-image" role="img" aria-label="Plate of blueberry muffins" style="left:55px;top:70px;width:400px;height:175px;background:radial-gradient(ellipse at 45% 50%, var(--muffin-tone) 0 35%, #f4ece6 55%, transparent 72%);"></div>
    <h2 class="panel-band" style="top:9px;padding-left:5px;">Something Light:</h2>
    <div class="row" style="top:55px"><span style="left:5px">Mixed Yoghurts</span><span style="left:288px">$5.50</span></div>
    <div class="row" style="top:75px"><span style="left:5px">Chia Pudding</span><span style="left:288px">$5.50</span></div>
    <div class="row" style="top:96px"><span style="left:5px">Fruit Salad</span><span style="left:288px">$5.50</span></div>
    <div class="row" style="top:116px"><span style="left:5px">Bircher Muesli</span><span style="left:288px">$5.50</span></div>
    <div class="row" style="top:137px"><span style="left:5px">Protein Balls</span><span style="left:288px">$4.0</span></div>
    <div class="row" style="top:157px"><span style="left:5px">Banana Bread</span><span style="left:288px">$4.50</span></div>
    <div class="row" style="top:178px"><span style="left:5px">Muffins</span><span style="left:288px">$4.50</span></div>
    <div class="row" style="top:199px"><span style="left:5px">Slices</span><span style="left:288px">$4.0</span></div>
  </section>

  <section class="panel breakfast-panel">
    <div class="food-image" role="img" aria-label="Breakfast plate with eggs, bacon, sausages and french toast" style="left:110px;top:55px;width:378px;height:210px;background:radial-gradient(ellipse at 55% 55%, var(--plate-tone) 0 35%, #f6efe9 58%, transparent 74%);"></div>
    <h2 class="panel-band" style="top:13px;padding-left:15px;">Breakfast Items:</h2>
    <div class="row" style="top:59px"><span style="left:15px">Bacon, Egg and Cheese Roll</span><span style="left:339px">$6.0</span></div>
    <div class="row" style="top:80px"><span style="left:15px">Ham and Cheese Toastie</span><span style="left:339px">$5.0</span></div>
    <div class="row" style="top:100px"><span style="left:15px">Cheese and Tomato Toastie</span><span style="left:339px">$5.0</span></div>
    <div class="row" style="top:121px"><span style="left:15px">Ham and Cheese Croissant</span><span style="left:339px">$6.0</span></div>
    <div class="row" style="top:142px"><span style="left:15px">Cheese and Tomato Croissant</span><span style="left:339px">$5.50</span></div>
    <div class="row" style="top:162px"><span style="left:15px">Plain Croissant</span><span style="left:339px">$3.50</span></div>
    <div class="row" style="top:183px"><span style="left:15px">Hash Brown</span><span style="left:339px">$2.0</span></div>
    <div class="row" style="top:203px"><span style="left:15px">2 Piece Toast</span><span style="left:339px">$3.0</span></div>
    <div class="row" style="top:224px"><span style="left:15px">2 Piece Rasin Toast</span><span style="left:339px">$3.0</span></div>
  </section>

  <section class="panel hot-panel">
    <div class="food-image" role="img" aria-label="Chicken wraps with hot chips and a dipping sauce" style="left:95px;top:60px;width:350px;height:250px;background:radial-gradient(ellipse at 55% 50%, var(--wrap-tone) 0 35%, #f3e8df 58%, transparent 74%);"></div>
    <h2 class="panel-band" style="top:20px;padding-left:26px;">Hot Food and Sandwiches:</h2>
    <div class="row" style="top:68px"><span style="left:26px">Pre Made Sandwiches</span><span style="left:350px">$6.50 &nbsp;- &nbsp;$7.50</span></div>
    <div class="row" style="top:88px"><span style="left:26px">Pre Made Focaccias</span><span style="left:350px">$8.50</span></div>
    <div class="row" style="top:109px"><span style="left:26px">Wraps</span><span style="left:350px">$7.50</span></div>
    <div class="row" style="top:129px"><span style="left:26px">Vegetarian Salad</span><span style="left:350px">$7.50</span></div>
    <div class="row" style="top:150px"><span style="left:26px">Meat/Seafood Salad</span><span style="left:350px">$9.50</span></div>
    <div class="row" style="top:170px"><span style="left:26px">Hot Chips</span><span style="left:350px">$4.50</span></div>
    <div class="row" style="top:191px"><span style="left:26px">Dim Sim</span><span style="left:350px">$1.50</span></div>
    <div class="row" style="top:211px"><span style="left:26px">Potato Cake</span><span style="left:350px">$1.50</span></div>
    <div class="row" style="top:232px"><span style="left:26px">Plain Hamburger</span><span style="left:350px">$7.50</span></div>
    <div class="row" style="top:253px"><span style="left:26px">Hamburger with the lot</span><span style="left:350px">$9.0</span></div>
    <div class="row" style="top:273px"><span style="left:26px">Chicken Schnitzel Burger</span><span style="left:350px">$8.50</span></div>
    <p class="store-note">Our Store inside the Hospital Food Court sells: Hot Pies,<br>Assorted Pasta's, Ready-to-go Meals, Quiche, and lots more!</p>
  </section>

  <div class="brand"><span class="brand-dot"></span><span class="brand-name">Ward Café</span></div>
</body>
</html>
```